coaching agenda

Please redesign the brochure attached in a more modern/trendy out look. I want something completely different to what is attached but using the same colours and logo.

```html
<!DOCTYPE html>
<html lang="en">
<head>
<meta charset="utf-8">
<title>Coaching Session – June 2018</title>
<link href="https://fonts.googleapis.com/css2?family=Ubuntu:wght@400;500;700&display=swap" rel="stylesheet">
<style>
  :root {
    --brand-blue: #15a3dc;
    --brand-dark: #3a3a3c;
    --text-grey: #4a4a4c;
    --paper: #ffffff;
    --photo-warm: #c9a58a;
    --photo-deep: #5a4a44;
    --photo-light: #e8e2da;
  }
  * { box-sizing: border-box; margin: 0; padding: 0; }
  html, body { width: 946px; height: 1200px; overflow: hidden; background: var(--paper); }
  body { font-family: "Ubuntu", sans-serif; }
  .flyer { position: relative; width: 946px; height: 1200px; background: var(--paper); overflow: hidden; }
  .hero { position: absolute; left: 0; top: 0; width: 946px; height: 720px; }
  .date-text { font-family: "Ubuntu", sans-serif; font-weight: 700; fill: var(--paper); font-size: 56px; text-anchor: middle; }
  .brand-name { font-family: "Ubuntu", sans-serif; font-weight: 500; fill: var(--brand-dark); font-size: 36px; text-anchor: middle; }
  .brand-sub { font-family: "Ubuntu", sans-serif; font-weight: 500; fill: var(--brand-dark); font-size: 13px; text-anchor: middle; letter-spacing: 0.5px; }
  .session-title { position: absolute; left: 128px; top: 724px; font-size: 42px; letter-spacing: 2px; color: var(--brand-dark); font-weight: 400; line-height: 50px; }
  .session-title strong { color: var(--brand-blue); font-weight: 700; }
  .title-rule { position: absolute; left: 116px; top: 782px; width: 718px; height: 3px; background: var(--brand-blue); }
  .title-rule::after { content: ""; position: absolute; right: -12px; top: -5px; width: 13px; height: 13px; background: var(--brand-blue); }
  .theme-bar { position: absolute; left: 116px; top: 810px; width: 730px; height: 44px; background: var(--brand-dark); color: var(--paper); font-weight: 700; font-size: 31px; letter-spacing: 2.8px; line-height: 44px; padding-left: 22px; white-space: nowrap; }
  .questions { position: absolute; left: 116px; top: 878px; width: 646px; list-style: none; }
  .questions li { position: relative; padding-left: 34px; font-size: 21.5px; line-height: 24px; color: var(--text-grey); margin-bottom: 13px; min-height: 48px; }
  .questions li::before { content: ""; position: absolute; left: 0; top: 4px; width: 12px; height: 39px; background: var(--brand-blue); }
  .questions li.single { padding-top: 14px; }
  .questions li.single::before { top: 4px; }
  .footer-band { position: absolute; left: 0; bottom: 0; width: 946px; height: 36px; background: var(--brand-blue); }
</style>
</head>
<body>
<main class="flyer">
  <svg class="hero" viewBox="0 0 946 720" xmlns="http://www.w3.org/2000/svg">
    <defs>
      <linearGradient id="photoTone" x1="0" y1="0" x2="1" y2="1">
        <stop offset="0" stop-color="var(--photo-deep)"/>
        <stop offset="0.45" stop-color="var(--photo-warm)"/>
        <stop offset="1" stop-color="var(--photo-light)"/>
      </linearGradient>
      <filter id="softShadow" x="-20%" y="-20%" width="140%" height="140%">
        <feDropShadow dx="0" dy="3" stdDeviation="5" flood-color="#000" flood-opacity="0.25"/>
      </filter>
    </defs>
    <circle class="photo-ring-outer" cx="270" cy="170" r="530" fill="var(--brand-blue)"/>
    <circle class="photo-ring-inner" cx="270" cy="170" r="495" fill="var(--brand-dark)"/>
    <circle class="photo-frame" cx="270" cy="170" r="460" fill="url(#photoTone)" role="img" aria-label="Photo of smiling students studying together at a classroom desk"/>
    <g class="brand-badge">
      <circle cx="680" cy="512" r="198" fill="var(--brand-blue)"/>
      <circle cx="680" cy="512" r="176" fill="var(--paper)" filter="url(#softShadow)"/>
      <text class="brand-name" x="684" y="594">Oliver Hart</text>
      <text class="brand-sub" x="684" y="622">Brightpath Coaching Co.</text>
    </g>
    <g class="date-badge">
      <circle cx="780" cy="298" r="130" fill="var(--brand-dark)"/>
      <circle cx="780" cy="298" r="115" fill="var(--brand-blue)"/>
      <text class="date-text" x="780" y="284">JUNE</text>
      <text class="date-text" x="780" y="350">2018</text>
    </g>
  </svg>

  <h1 class="session-title"><strong>COACHING</strong> SESSION</h1>
  <div class="title-rule"></div>
  <div class="theme-bar">YESTERDAY – TODAY – TOMORROW</div>

  <ul class="questions">
    <li>How many appraisals/listing presentations are booked in your diary for this week?</li>
    <li>How many appraisals/listing presentations are booked in your diary for next week?</li>
    <li>How many second viewings/private viewings are booked in your diary for this week?</li>
    <li class="single">How many listings will you launch this week?</li>
  </ul>

  <div class="footer-band"></div>
</main>
</body>
</html>
```